Wanting a leaflet that can be letter boxed to surronding areas to my workshop.

Will need it to display -
Tarrow Automotive Location

Contact details- (maybe even a little street map?)
4/6-8 Quenby Place,
Fernlea Heights
9358 2491
info@tarrowauto-example.com.au
www.tarrowauto-example.com.au

Services include -
Log book servicing
Mechanical repairs
Pre sale inspections
Great Service and Advice
Weeekend Servicing (This needs to be a big point to get across)

Service Special - $179*
Includes
Engine Oil and filter replacement using factory approved parts
Wheel rotation
Brake inspection
Cooling system test
Saftey inspection

*Large cars $249

Target Market(s)

People in areas close to workshop location, uni students, performance cars, parents

Industry/Entity Type

Automotive

Requirements
Must have
• Tarrow Automotive logo

```html
<!DOCTYPE html>
<html lang="en">
<head>
<meta charset="utf-8">
<title>Tarrow Automotive – Quality Auto Services</title>
<link rel="stylesheet" href="https://fonts.googleapis.com/css2?family=Open+Sans:ital,wght@0,400;0,600;0,700;0,800;1,400;1,600&display=swap">
<style>
  :root {
    --ink-dark: #120406;
    --maroon: #3a070c;
    --deep-red: #5c0c13;
    --brand-red: #c3111e;
    --brand-red-dark: #8c0a14;
    --accent-red: #d8141f;
    --silver-light: #f2f2f2;
    --silver-mid: #a9a9a9;
    --silver-dark: #6a6a6a;
    --grille-dark: #1c1c1e;
    --grille-mid: #4a4a4d;
    --white: #ffffff;
  }
  html, body {
    margin: 0;
    padding: 0;
    width: 856px;
    height: 1200px;
    overflow: hidden;
    background: #1a0507;
  }
  .leaflet {
    position: relative;
    width: 856px;
    height: 1200px;
    overflow: hidden;
    font-family: "Open Sans", Arial, sans-serif;
    color: var(--white);
    background:
      radial-gradient(ellipse 70% 45% at 50% 62%, var(--deep-red) 0%, rgba(92,12,19,0) 80%),
      linear-gradient(180deg, var(--ink-dark) 0%, #2a0508 28%, var(--maroon) 55%, #2a0508 85%, var(--ink-dark) 100%);
  }

  /* Header grille area with name */
  .hero-grille {
    position: absolute;
    left: 80px;
    top: 16px;
    width: 717px;
    height: 360px;
    border-radius: 70px 70px 120px 120px / 60px 60px 160px 160px;
    background:
      radial-gradient(ellipse 60% 55% at 50% 45%, var(--grille-mid) 0%, var(--grille-dark) 75%),
      var(--grille-dark);
    box-shadow: inset 0 0 0 10px #8d8d90, inset 0 0 0 14px #2b2b2d, 0 10px 30px rgba(0,0,0,.7);
  }
  .site-url-top {
    position: absolute;
    top: 40px;
    left: 0;
    width: 856px;
    margin: 0;
    text-align: center;
    font-size: 18px;
    letter-spacing: 8.5px;
    color: var(--accent-red);
    font-weight: 400;
  }
  .brand-name {
    position: absolute;
    top: 200px;
    left: 0;
    width: 856px;
    text-align: center;
    color: var(--silver-light);
    font-weight: 800;
    line-height: 1;
    text-transform: uppercase;
  }
  .brand-name .brand-main {
    display: block;
    font-size: 84px;
    letter-spacing: 2px;
  }
  .brand-name .brand-sub {
    display: block;
    margin-top: 10px;
    font-size: 30px;
    letter-spacing: 26px;
    padding-left: 26px;
  }

  /* Headline */
  .headline {
    position: absolute;
    top: 400px;
    left: 0;
    width: 856px;
    margin: 0;
    text-align: center;
    font-size: 55px;
    font-weight: 800;
    letter-spacing: -0.5px;
    color: var(--silver-light);
    background: linear-gradient(180deg, #ffffff 0%, #e6e6e6 45%, #9b9b9b 55%, #dcdcdc 100%);
    -webkit-background-clip: text;
    background-clip: text;
    -webkit-text-fill-color: transparent;
    filter: drop-shadow(0 3px 3px rgba(0,0,0,.8));
  }

  /* Car photo backdrop */
  .car-photo {
    position: absolute;
    left: 43px;
    top: 660px;
    width: 770px;
    height: 325px;
    border-radius: 40% 50% 20% 20% / 45% 55% 15% 15%;
    background: radial-gradient(ellipse 60% 55% at 52% 50%, rgba(190,30,40,.55) 0%, rgba(120,14,22,.35) 55%, rgba(60,8,12,0) 100%);
  }

  /* Section headers */
  .panel-tab {
    position: absolute;
    top: 508px;
    height: 96px;
    margin: 0;
    padding: 14px 0 0 18px;
    box-sizing: border-box;
    font-size: 30px;
    font-weight: 700;
    line-height: 33px;
    text-transform: uppercase;
    clip-path: polygon(0 0, calc(100% - 22px) 0, 100% 22px, 100% 100%, 0 100%);
  }
  .panel-tab--services {
    left: 98px;
    width: 319px;
    background: linear-gradient(180deg, #cfcfcf 0%, var(--silver-mid) 50%, var(--silver-dark) 100%);
    color: var(--white);
    text-shadow: 0 2px 3px rgba(0,0,0,.85), 0 0 6px rgba(0,0,0,.45);
  }
  .panel-tab--special {
    left: 462px;
    width: 296px;
    background: linear-gradient(180deg, #e11a27 0%, var(--brand-red) 50%, var(--brand-red-dark) 100%);
    color: var(--white);
    text-shadow: 0 2px 3px rgba(0,0,0,.45);
  }
  .tab-underline {
    position: absolute;
    top: 608px;
    height: 3px;
    background: linear-gradient(90deg, rgba(255,255,255,.1), #cfcfcf, rgba(255,255,255,.1));
  }
  .tab-underline--services { left: 98px; width: 319px; }
  .tab-underline--special { left: 462px; width: 296px; }
  .tools-icon {
    position: absolute;
    left: 421px;
    top: 542px;
    width: 38px;
    height: 38px;
  }

  /* Lists */
  .service-list {
    position: absolute;
    margin: 0;
    padding: 0;
    list-style: none;
    font-weight: 700;
    font-size: 28px;
    line-height: 31px;
    text-shadow: 0 2px 4px rgba(0,0,0,.75);
  }
  .service-list li {
    position: relative;
    padding-left: 18px;
  }
  .service-list li::before {
    content: "";
    position: absolute;
    left: 0;
    top: 6px;
    width: 7px;
    height: 18px;
    background: var(--accent-red);
    clip-path: polygon(0 0, 100% 30%, 100% 100%, 0 70%);
  }
  .service-list--included {
    left: 96px;
    top: 636px;
    width: 330px;
  }
  .service-list--included li { margin-bottom: 24px; }
  .service-list--included .emphasis { text-transform: uppercase; }

  .service-list--special {
    left: 460px;
    top: 636px;
    width: 340px;
  }
  .service-list--special li { margin-bottom: 25px; }
  .service-list--special li:nth-child(3) { margin-bottom: 28px; }
  .fine-print {
    position: absolute;
    left: 486px;
    top: 944px;
    margin: 0;
    font-size: 20px;
    font-style: italic;
    color: #f1f1f1;
  }

  /* Contact block */
  .contact-card {
    position: absolute;
    left: 98px;
    top: 993px;
    width: 651px;
    height: 139px;
    margin: 0;
    box-sizing: border-box;
    padding: 12px 0 0 16px;
    background: linear-gradient(180deg, #d4141f 0%, var(--brand-red) 45%, var(--brand-red-dark) 100%);
    clip-path: polygon(0 0, calc(100% - 22px) 0, 100% 22px, 100% 100%, 0 100%);
  }
  .contact-card p { margin: 0; }
  .contact-address, .contact-email {
    font-size: 25px;
    line-height: 30px;
    font-weight: 400;
  }
  .contact-web {
    font-size: 25px;
    line-height: 30px;
    font-weight: 700;
  }
  .contact-tagline {
    font-size: 17px;
    font-style: italic;
    letter-spacing: 3px;
    line-height: 24px;
  }
  .contact-brand {
    position: absolute;
    right: 42px;
    top: 68px;
    text-align: center;
    font-weight: 800;
    color: var(--white);
    text-transform: uppercase;
    line-height: 1;
  }
  .contact-brand .brand-main { display: block; font-size: 28px; }
  .contact-brand .brand-sub { display: block; font-size: 11px; letter-spacing: 6px; margin-top: 3px; }
  .contact-rule {
    position: absolute;
    left: 98px;
    top: 1134px;
    width: 651px;
    height: 3px;
    background: linear-gradient(90deg, rgba(255,255,255,.05), #bdbdbd, rgba(255,255,255,.05));
  }
</style>
</head>
<body>
<main class="leaflet">
  <div class="hero-grille" role="img" aria-label="Chrome-framed mesh car grille behind the business name"></div>
  <p class="site-url-top">www.tarrowauto-example.com.au</p>
  <div class="brand-name" aria-label="Tarrow Automotive">
    <span class="brand-main">Tarrow</span>
    <span class="brand-sub">Automotive</span>
  </div>

  <h1 class="headline">QUALITY AUTO SERVICES</h1>

  <div class="car-photo" role="img" aria-label="Red hatchback car photo in the background"></div>

  <h2 class="panel-tab panel-tab--services">Services<br>Include</h2>
  <div class="tab-underline tab-underline--services"></div>

  <svg class="tools-icon" viewBox="0 0 44 44" aria-hidden="true">
    <g stroke-linecap="round">
      <line x1="8" y1="36" x2="30" y2="14" stroke="#dcdcdc" stroke-width="6"/>
      <circle cx="33" cy="11" r="7" fill="#dcdcdc"/>
      <circle cx="35" cy="9" r="3.5" fill="#2a0508"/>
      <line x1="36" y1="36" x2="18" y2="18" stroke="#1d1d1d" stroke-width="7"/>
      <line x1="16" y1="16" x2="8" y2="8" stroke="#cfcfcf" stroke-width="3"/>
    </g>
  </svg>

  <h2 class="panel-tab panel-tab--special">Service<br>Special - $179*</h2>
  <div class="tab-underline tab-underline--special"></div>

  <ul class="service-list service-list--included">
    <li>Log book servicing</li>
    <li>Mechanical repairs</li>
    <li>Pre sale inspections</li>
    <li>Great Service and Advice</li>
    <li class="emphasis">Weeekend<br>Servicing</li>
  </ul>

  <ul class="service-list service-list--special">
    <li>Engine Oil and filter replacement using factory approved parts</li>
    <li>Wheel rotation</li>
    <li>Brake inspection</li>
    <li>Cooling system test Saftey inspection</li>
  </ul>
  <p class="fine-print">*Large cars $249</p>

  <section class="contact-card">
    <p class="contact-address">4/6-8 Quenby Place, Fernlea Heights 9358 2491</p>
    <p class="contact-email">info@tarrowauto-example.com.au</p>
    <p class="contact-web">www.tarrowauto-example.com.au</p>
    <p class="contact-tagline">visit our web and find us at the map</p>
    <div class="contact-brand" aria-label="Tarrow Automotive">
      <span class="brand-main">Tarrow</span>
      <span class="brand-sub">Automotive</span>
    </div>
  </section>
  <div class="contact-rule"></div>
</main>
</body>
</html>
```